Design a business card (front and back) for a Technology Consulting firm. Preference is for a clean look - professional, favour minimalist rather than something busy. two logos are attached. You can use any of them. . The information below is for the purpose of presenting an entry in the contest, but the winner will be given correct information to product another version of the entry. The winner will also be given an opportunity to prepare a letterhead (ideally consistent with the business card).

Mara Colvin
Partner
+61 438 902 617
+61 7 3986 2150
jane@[url removed, login to view]
[url removed, login to view]
GPO Box 8362
Brisbane QLD 4009

The winning entry should be in a format that most business card printers can easily print.

```html
<!DOCTYPE html>
<html lang="en">
<head>
<meta charset="utf-8">
<title>KTR Consulting Services – Business Card</title>
<link href="https://fonts.googleapis.com/css2?family=Arimo:wght@400;700&family=Montserrat:wght@700;800&display=swap" rel="stylesheet">
<style>
  :root {
    --page-bg: #e9eaec;
    --brand-blue: #2a95d1;
    --brand-blue-deep: #1f82c0;
    --ink: #1d1d1f;
    --ink-soft: #2f2f33;
    --paper: #ffffff;
    --strip: #111111;
    --white: #ffffff;
  }
  * { box-sizing: border-box; margin: 0; padding: 0; }
  html, body {
    width: 1200px; height: 799px; overflow: hidden;
    background: var(--page-bg);
  }
  .sheet {
    position: relative; width: 1200px; height: 799px;
    display: flex; align-items: center; justify-content: center; gap: 50px;
  }
  .card {
    position: relative; width: 520px; height: 316px;
    overflow: hidden;
    box-shadow: 0 10px 28px rgba(0,0,0,0.18);
  }

  /* Back of card */
  .card--back { background: var(--brand-blue); color: var(--white); }
  .back-mark {
    position: absolute; left: 44px; top: 118px;
    font-family: "Montserrat", sans-serif; font-weight: 800;
    font-size: 64px; letter-spacing: 2px; color: var(--white);
  }
  .back-divider {
    position: absolute; left: 220px; top: 104px;
    width: 2px; height: 96px; background: var(--white);
  }
  .back-company {
    position: absolute; left: 236px; top: 104px;
    font-family: "Montserrat", sans-serif; font-weight: 700;
    font-size: 24px; line-height: 26px; text-transform: uppercase; letter-spacing: 0.5px;
  }
  .back-tagline {
    position: absolute; left: 237px; top: 163px;
    font-family: "Montserrat", sans-serif; font-weight: 700;
    font-size: 10px; letter-spacing: 1.6px; text-transform: uppercase;
  }
  .back-rule {
    position: absolute; left: 236px; top: 182px;
    width: 220px; height: 1.5px; background: var(--white);
  }
  .back-web {
    position: absolute; left: 236px; top: 240px;
    font-family: "Arimo", sans-serif; font-size: 14px; letter-spacing: 0.3px;
  }

  /* Front of card */
  .card--front { background: var(--paper); color: var(--ink); }
  .front-strip {
    position: absolute; left: 0; top: 0; width: 16px; height: 100%;
    background: var(--strip);
  }
  .front-band {
    position: absolute; left: 16px; right: 0; bottom: 0; height: 12px;
    background: var(--brand-blue);
  }
  .front-mark {
    position: absolute; left: 42px; top: 26px;
    font-family: "Montserrat", sans-serif; font-weight: 800;
    font-size: 30px; letter-spacing: 1px; color: var(--brand-blue-deep);
  }
  .person {
    position: absolute; left: 352px; top: 40px;
    font-family: "Arimo", sans-serif; font-size: 19px; line-height: 22px;
    color: var(--ink-soft);
  }
  .contact-list {
    position: absolute; left: 40px; top: 140px; list-style: none;
    font-family: "Arimo", sans-serif; font-size: 13.5px; line-height: 17px;
    color: var(--ink);
  }
  .contact-item { display: flex; align-items: flex-start; gap: 20px; margin-bottom: 16px; }
  .contact-icon { width: 20px; height: 22px; flex: none; }
</style>
</head>
<body>
<main class="sheet">
  <section class="card card--back" aria-label="Card back">
    <div class="back-mark">KTR</div>
    <div class="back-divider"></div>
    <div class="back-company">KTR Consulting<br>Services Ltd</div>
    <div class="back-tagline">Insight in Practice</div>
    <div class="back-rule"></div>
    <div class="back-web">www.velmoracon.com</div>
  </section>

  <section class="card card--front" aria-label="Card front">
    <div class="front-strip"></div>
    <div class="front-band"></div>
    <div class="front-mark">KTR</div>
    <div class="person">Mara Colvin<br>Partner</div>
    <ul class="contact-list">
      <li class="contact-item">
        <svg class="contact-icon" viewBox="0 0 20 22" aria-hidden="true">
          <path d="M10 2a6 6 0 0 0-6 6c0 4.5 6 11 6 11s6-6.5 6-11a6 6 0 0 0-6-6z" fill="none" stroke="#2a95d1" stroke-width="1.6"/>
          <circle cx="10" cy="8" r="2.2" fill="none" stroke="#2a95d1" stroke-width="1.6"/>
        </svg>
        <span>GPO Box 8362<br>Brisbane QLD 4009</span>
      </li>
      <li class="contact-item">
        <svg class="contact-icon" viewBox="0 0 20 22" aria-hidden="true">
          <circle cx="10" cy="10" r="9" fill="#2a95d1"/>
          <circle cx="10" cy="10" r="3" fill="none" stroke="#fff" stroke-width="1.6"/>
          <path d="M13 7v4.2c0 1.4 2.6 1.4 2.6-1.2A5.6 5.6 0 1 0 12.5 15" fill="none" stroke="#fff" stroke-width="1.6"/>
        </svg>
        <span>mara@velmoracon.com</span>
      </li>
      <li class="contact-item">
        <svg class="contact-icon" viewBox="0 0 20 22" aria-hidden="true">
          <rect x="5" y="1.5" width="10" height="19" rx="2" fill="none" stroke="#2a95d1" stroke-width="1.6"/>
          <line x1="5" y1="4.5" x2="15" y2="4.5" stroke="#2a95d1" stroke-width="1.2"/>
          <line x1="5" y1="16.5" x2="15" y2="16.5" stroke="#2a95d1" stroke-width="1.2"/>
          <circle cx="10" cy="18.6" r="0.9" fill="#2a95d1"/>
        </svg>
        <span>+61 438 902 617<br>+61 7 3986 2150</span>
      </li>
    </ul>
  </section>
</main>
</body>
</html>
```